Maple Hollow Bloom Panels Business card

Looking to have a business card design incorporating my logo for my flower wall business.

Industry/Entity Type

Wedding & event planning

Contact Information for Business Card

My business logo, my name - Lena Whitcombe (owner), my tagline - Let us be your something extra, phone # 401-726-3148, email address - maplehollowbloompanels@mailvane.net, my website - maplehollowbloompanels.net, Instagram handle- @maplehollowbloompanels, FB handle Handle - maplehollowbloompanels

Font styles to use
Other font styles liked:
• Sentaina is the font that is used in my logo

Requirements
Must have
• Would like a double sided business card

```html
<!DOCTYPE html>
<html lang="en">
<head>
<meta charset="utf-8">
<title>Maple Hollow Bloom Panels – Business Card</title>
<link rel="stylesheet" href="https://fonts.googleapis.com/css2?family=Allura&family=Cormorant+Garamond:ital,wght@0,500;1,500&family=Lora:wght@400&display=swap">
<style>
  :root {
    --backdrop: #e6cfd2;
    --card-white: #fbfafa;
    --rose: #e8739c;
    --blush: #f4c6d6;
    --blush-soft: #f3dde5;
    --ink: #555055;
    --dot: #e8739c;
  }
  * { margin: 0; padding: 0; box-sizing: border-box; }
  html, body {
    width: 1200px; height: 1000px; overflow: hidden;
    background: var(--backdrop);
  }
  .canvas {
    position: relative; width: 1200px; height: 1000px;
  }
  .card {
    position: absolute; top: 338px;
    width: 540px; height: 325px;
    background: var(--card-white);
    box-shadow: 0 8px 18px rgba(120, 80, 90, 0.25);
    overflow: hidden;
  }
  .card--back { left: 45px; }
  .card--front { left: 615px; }

  /* Back side */
  .back-pattern {
    position: absolute; left: 16px; top: 16px; right: 16px; bottom: 16px;
    background: linear-gradient(135deg, var(--blush) 0%, #f7d3df 50%, var(--blush) 100%);
  }
  .back-panel {
    position: absolute; left: 146px; top: 0; width: 272px; height: 194px;
    background: var(--rose);
    display: flex; align-items: center; justify-content: center; gap: 10px;
  }
  .back-panel .brand-mark {
    width: 14px; height: 14px; border-radius: 50%;
    background: var(--card-white); flex: none;
  }
  .back-panel .brand-name {
    font-family: "Cormorant Garamond", serif; font-weight: 500;
    font-size: 22px; line-height: 1.15; color: var(--card-white);
    text-align: center; letter-spacing: 0.5px;
  }
  .back-web {
    position: absolute; left: 146px; top: 275px; width: 272px; height: 34px;
    background: var(--card-white);
    display: flex; align-items: center; justify-content: center;
    font-family: "Lora", serif; font-size: 14px; color: var(--ink); letter-spacing: 0.6px;
  }

  /* Front side */
  .front-pattern {
    position: absolute; inset: 0;
    background: linear-gradient(160deg, var(--card-white) 0%, var(--blush-soft) 50%, var(--card-white) 100%);
    opacity: 0.7;
  }
  .front-logo {
    position: absolute; top: 32px; left: 0; right: 0;
    display: flex; align-items: center; justify-content: center; gap: 8px;
  }
  .front-logo .brand-mark {
    width: 12px; height: 12px; border-radius: 50%; background: var(--rose);
  }
  .front-logo .brand-name {
    font-family: "Cormorant Garamond", serif; font-weight: 500;
    font-size: 19px; color: var(--ink); letter-spacing: 0.5px;
  }
  .tagline {
    position: absolute; top: 112px; left: 0; right: 0;
    text-align: center;
    font-family: "Cormorant Garamond", serif; font-style: italic; font-weight: 500;
    font-size: 15px; letter-spacing: 2px; color: var(--ink);
  }
  .tagline .dot { color: var(--dot); margin: 0 8px; }
  .name-band {
    position: absolute; top: 153px; left: 0; right: 0; height: 86px;
    background: var(--rose);
    display: flex; align-items: center; justify-content: center;
  }
  .name-band .owner {
    font-family: "Allura", cursive; font-size: 50px; color: var(--card-white);
  }
  .contact-line {
    position: absolute; top: 254px; left: 0; right: 0; text-align: center;
    font-family: "Lora", serif; font-size: 14px; color: var(--ink); letter-spacing: 0.4px;
  }
  .contact-line .sep { margin: 0 6px; }
  .social-line {
    position: absolute; top: 280px; left: 0; right: 0;
    display: flex; align-items: center; justify-content: center; gap: 8px;
    font-family: "Lora", serif; font-size: 14px; color: var(--ink); letter-spacing: 0.6px;
  }
  .social-line .social-dot {
    width: 14px; height: 14px; border-radius: 50%; background: var(--rose);
  }
</style>
</head>
<body>
<main class="canvas">
  <section class="card card--back" aria-label="Business card back">
    <div class="back-pattern" role="img" aria-label="Soft pink leaf and berry pattern"></div>
    <div class="back-panel">
      <span class="brand-mark"></span>
      <span class="brand-name">Maple Hollow<br>Bloom Panels</span>
    </div>
    <div class="back-web">maplehollowbloompanels.net</div>
  </section>

  <section class="card card--front" aria-label="Business card front">
    <div class="front-pattern" role="img" aria-label="Faint pink leaf pattern"></div>
    <div class="front-logo">
      <span class="brand-mark"></span>
      <span class="brand-name">Maple Hollow Bloom Panels</span>
    </div>
    <p class="tagline"><span class="dot">•</span>let us be your something extra<span class="dot">•</span></p>
    <div class="name-band"><span class="owner">Lena Whitcombe</span></div>
    <p class="contact-line">401-726-3148<span class="sep">|</span>maplehollowbloompanels@mailvane.net</p>
    <p class="social-line"><span class="social-dot"></span>maplehollowbloompanels</p>
  </section>
</main>
</body>
</html>
```